Criação de Papelaria (6 itens) para Beleza
" Somos uma Distribuidora de Cosméticos. Compramos os produtos diretamente das Indústrias e depois revendemos para lojistas em MG e no Norte do Rio. Antes, nós éramos uma distribuidora apenas da marca Vorani (https://www.voranicosmeticos.com.br/). Por esse motivo, utilizávamos uma logo feita pelo marketing deles, nas cores deles, para que as duas logos sempre andassem casadas. Hoje, ampliamos o nosso mix e distribuímos também os produtos da Mirtex ( https://www.mirtex.com.br/) e da henna Sol de Jade. Ou seja, hoje somos efetivamente uma distribuidora de Cosméticos em geral, atendendo os michos de cabelo, pele, maquiagem e unhas. Dessa maneira, criamos uma nova logo, para representar a Distribuidora. "

```html
<!DOCTYPE html>
<html lang="pt-BR">
<head>
<meta charset="UTF-8">
<title>Lumiera — Papel Timbrado</title>
<link rel="stylesheet" href="https://fonts.googleapis.com/css2?family=Montserrat:wght@300;400;500&display=swap">
<style>
  :root {
    --backdrop: #ececee;
    --paper: #ffffff;
    --paper-shade: #f6f6f7;
    --gold: #b89a5e;
    --gold-light: #d8c394;
    --ink: #4a4d55;
    --ink-soft: #8a8d94;
    --navy: #1d2331;
  }
  * { margin: 0; padding: 0; box-sizing: border-box; }
  html, body {
    width: 1200px; height: 1200px; overflow: hidden;
    background: var(--backdrop);
    font-family: "Montserrat", sans-serif;
  }
  .canvas {
    width: 1200px; height: 1200px;
    display: flex; align-items: center; justify-content: center;
  }
  .letterhead {
    position: relative;
    width: 792px; height: 1120px;
    background: linear-gradient(160deg, var(--paper) 0%, var(--paper-shade) 100%);
    box-shadow: 0 12px 40px rgba(0,0,0,0.10);
  }
  .brand {
    position: absolute; top: 96px; left: 0; right: 0;
    display: flex; flex-direction: column; align-items: center;
  }
  .brand-row { display: flex; align-items: center; gap: 14px; }
  .brand-dot {
    width: 34px; height: 34px; border-radius: 50%;
    border: 2px solid var(--gold);
  }
  .brand-name {
    font-weight: 300; font-size: 38px; letter-spacing: 4px;
    color: var(--ink); text-transform: uppercase;
  }
  .brand-tagline {
    margin-top: 4px; margin-left: 48px;
    font-weight: 400; font-size: 9px; letter-spacing: 2.4px;
    color: var(--ink-soft); text-transform: uppercase;
  }
  .contact {
    position: absolute; left: 56px; bottom: 96px;
    list-style: none;
    display: flex; flex-direction: column; gap: 9px;
  }
  .contact-item {
    display: flex; align-items: center; gap: 10px;
    font-size: 10px; line-height: 1.3; color: var(--ink);
  }
  .contact-icon {
    width: 18px; height: 18px; border-radius: 50%;
    background: var(--navy);
    display: flex; align-items: center; justify-content: center;
    flex-shrink: 0;
  }
  .contact-icon svg { width: 10px; height: 10px; }
  .footer-rule {
    position: absolute; left: 0; right: 0; bottom: 58px;
    height: 2px;
    background: linear-gradient(90deg, transparent 30%, var(--gold-light) 55%, var(--gold) 100%);
  }
  .footer-band {
    position: absolute; left: 0; right: 0; bottom: 30px;
    height: 16px; background: var(--navy);
  }
</style>
</head>
<body>
<main class="canvas">
  <article class="letterhead">
    <header class="brand">
      <div class="brand-row">
        <span class="brand-dot"></span>
        <span class="brand-name">Lumiera</span>
      </div>
      <span class="brand-tagline">Distribuidora de Cosméticos</span>
    </header>

    <ul class="contact">
      <li class="contact-item">
        <span class="contact-icon">
          <svg viewBox="0 0 24 24" fill="#fff"><path d="M6.6 10.8a15 15 0 0 0 6.6 6.6l2.2-2.2c.3-.3.7-.4 1-.2 1.1.4 2.3.6 3.6.6.6 0 1 .4 1 1V20c0 .6-.4 1-1 1A17 17 0 0 1 3 4c0-.6.4-1 1-1h3.5c.6 0 1 .4 1 1 0 1.3.2 2.5.6 3.6.1.3 0 .7-.2 1z"/></svg>
        </span>
        (00) 4820-7316
      </li>
      <li class="contact-item">
        <span class="contact-icon">
          <svg viewBox="0 0 24 24" fill="none" stroke="#fff" stroke-width="2.4"><rect x="3" y="5" width="18" height="14" rx="1"/><path d="M3 6l9 7 9-7"/></svg>
        </span>
        contato@lumieradistribuidora.com.br
      </li>
      <li class="contact-item">
        <span class="contact-icon">
          <svg viewBox="0 0 24 24" fill="#fff"><path d="M12 2a7 7 0 0 0-7 7c0 5.2 7 13 7 13s7-7.8 7-13a7 7 0 0 0-7-7zm0 9.5A2.5 2.5 0 1 1 12 6.5a2.5 2.5 0 0 1 0 5z"/></svg>
        </span>
        <span>Rua Jasmim do Vale, 48 - Jardim Aurora<br>Vale Sereno - UF - CEP 00000-000</span>
      </li>
    </ul>

    <div class="footer-rule"></div>
    <div class="footer-band"></div>
  </article>
</main>
</body>
</html>
```